Vantorel Business Card

I want a business card for me and my employees.
On one side it must be in Greek and on the other side in English. The color must much the one of the logo

Target Market(s)

Customers that are looking for security and antipiracy advisors

Contact Information for Business Card

Title, Email, Phone, website , Mobile Address Zip code, city and country

Requirements
Must have
• The colors of our logo (the blue ones)

```html
<!DOCTYPE html>
<html lang="en">
<head>
<meta charset="utf-8">
<title>Vantorel Advisory Business Card</title>
<link href="https://fonts.googleapis.com/css2?family=Montserrat:wght@500&family=Roboto:wght@400;500&display=swap" rel="stylesheet">
<style>
  :root {
    --navy: #27245c;
    --white: #ffffff;
    --paper: #fbfbfb;
    --canvas: #efefef;
    --url: #5b5886;
    --edge: #3a3a3a;
  }
  * { margin: 0; padding: 0; box-sizing: border-box; }
  html, body {
    width: 1200px; height: 1052px; overflow: hidden;
    background: var(--canvas);
  }
  .canvas { position: relative; width: 1200px; height: 1052px; }

  .card { position: absolute; left: 324px; width: 552px; height: 334px; overflow: hidden; }

  /* Front */
  .card-front { top: 142px; background: var(--navy); }
  .brand {
    position: absolute; display: flex; align-items: center;
    font-family: "Montserrat", sans-serif; font-weight: 500; text-transform: uppercase;
  }
  .brand-mark { display: block; flex: none; }
  .brand-name { display: flex; flex-direction: column; line-height: 1; }
  .card-front .brand { left: 132px; top: 115px; gap: 18px; color: var(--white); }
  .card-front .brand-mark { width: 68px; height: 94px; background: var(--white); }
  .card-front .brand-name { font-size: 38px; letter-spacing: 2px; gap: 10px; }
  .front-url {
    position: absolute; left: 0; right: 0; top: 300px; text-align: center;
    font-family: "Roboto", sans-serif; font-size: 14px; letter-spacing: 9.4px;
    color: var(--url); padding-left: 10px;
  }

  /* Back */
  .card-back { top: 546px; background: var(--paper); border: 1px solid var(--edge); }
  .back-band { position: absolute; left: 0; right: 0; top: 149px; bottom: 0; background: var(--navy); }
  .card-back .brand { left: 25px; top: 31px; gap: 14px; color: var(--navy); }
  .card-back .brand-mark { width: 62px; height: 86px; background: var(--navy); }
  .card-back .brand-name { font-size: 33px; letter-spacing: 2px; gap: 10px; }
  .back-tile { position: absolute; left: 421px; top: 85px; width: 91px; height: 114px; background: var(--white); }

  .contact {
    position: absolute; left: 25px; top: 174px; color: var(--white);
    font-family: "Roboto", sans-serif;
  }
  .contact-name { font-size: 18.5px; font-weight: 500; line-height: 24px; }
  .contact-title { font-size: 14px; line-height: 18px; margin-top: 1px; }
  .contact-lines { margin-top: 17px; font-size: 13.5px; line-height: 17px; }
  .contact-lines .sep { padding: 0 10px; }
</style>
</head>
<body>
<div class="canvas">

  <section class="card card-front" aria-label="Card front">
    <div class="brand">
      <span class="brand-mark"></span>
      <span class="brand-name"><span>Vantorel</span><span>Advisory</span></span>
    </div>
    <p class="front-url">www.vantoreladvisory.com</p>
  </section>

  <section class="card card-back" aria-label="Card back">
    <div class="back-band"></div>
    <div class="brand">
      <span class="brand-mark"></span>
      <span class="brand-name"><span>Vantorel</span><span>Advisory</span></span>
    </div>
    <div class="back-tile"></div>
    <div class="contact">
      <p class="contact-name">John Doe Smith/Τζον Ντόε Σμιθ</p>
      <p class="contact-title">Managing Director/Διευθύνων Σύμβουλος</p>
      <div class="contact-lines">
        <p>P.: 828-111-1111</p>
        <p>E: john@yourwebsite.com<span class="sep">|</span>W: www.yourwebsite.com</p>
        <p>234 Anywhere St., Any City, Any Town, US 123456</p>
        <p>234 Οπουδήποτε St., οποιαδήποτε πόλη, Οποιαδήποτε πόλη, ΗΠΑ 123456</p>
      </div>
    </div>
  </section>

</div>
</body>
</html>
```